Business Card Design for a Design/Build Firm

Harrowgate Structures Group, Inc. is a firm providing construction professional project management and architectural design services to an international clientele. Contemporary. "Green" movement aware. Business card to have back design/logo. Cards will be on high gloss paper

Target Market(s)

Building Developers and Owners

Industry/Entity Type

Construction

Requirements
Nice to have
• We really would like to use the acronym "HSG" as main focal point fo card design. Company will be known as HSG.
Should not have
• No globes or abstract images of buildings.

```html
<!DOCTYPE html>
<html lang="en">
<head>
<meta charset="utf-8">
<title>HSG Business Card</title>
<link rel="stylesheet" href="https://fonts.googleapis.com/css2?family=Cinzel:wght@600&family=Open+Sans:wght@400&display=swap">
<style>
  :root {
    --bg: #e4e5e7;
    --paper: #ffffff;
    --green: #1f7a26;
    --green-light: #137a1f;
    --green-dark: #05501a;
    --ink-grey: #6f6f6f;
    --white: #ffffff;
  }
  * { box-sizing: border-box; margin: 0; padding: 0; }
  html, body { width: 1200px; height: 960px; overflow: hidden; }
  body {
    background: var(--bg);
    position: relative;
    font-family: "Open Sans", Arial, sans-serif;
  }
  .card {
    position: absolute;
    left: 320px;
    width: 560px;
    height: 320px;
    border-radius: 18px;
    box-shadow: 0 6px 18px rgba(0,0,0,0.18);
    overflow: hidden;
  }
  .card-front { top: 120px; background: var(--paper); }
  .card-back {
    top: 520px;
    background: linear-gradient(135deg, var(--green-light) 0%, var(--green-dark) 100%);
  }

  /* front */
  .front-mark {
    position: absolute;
    top: 30px;
    right: 40px;
    display: flex;
    align-items: center;
    gap: 10px;
    color: var(--green);
    font-family: "Cinzel", Georgia, serif;
    font-weight: 600;
  }
  .mark-square { width: 22px; height: 22px; background: var(--green); }
  .front-mark .mark-name { font-size: 38px; letter-spacing: 8px; line-height: 1; }
  .front-rule {
    position: absolute;
    top: 100px;
    left: 40px;
    right: 40px;
    height: 1px;
    background: var(--green);
  }
  .contact {
    position: absolute;
    left: 40px;
    bottom: 34px;
  }
  .contact-name {
    font-family: "Cinzel", Georgia, serif;
    font-weight: 600;
    font-size: 24px;
    color: var(--green);
    letter-spacing: 1px;
  }
  .contact-role {
    font-size: 12px;
    color: var(--ink-grey);
    padding-bottom: 6px;
    border-bottom: 1px solid var(--green);
    width: 200px;
    margin-bottom: 10px;
  }
  .contact-list { list-style: none; }
  .contact-list li {
    display: flex;
    align-items: center;
    gap: 10px;
    font-family: "Cinzel", Georgia, serif;
    font-size: 12px;
    color: var(--ink-grey);
    line-height: 22px;
  }
  .contact-list svg { width: 14px; height: 14px; fill: var(--green); }

  /* back */
  .back-mark {
    position: absolute;
    inset: 0;
    display: flex;
    flex-direction: column;
    align-items: center;
    justify-content: center;
    gap: 14px;
    color: var(--white);
    font-family: "Cinzel", Georgia, serif;
    font-weight: 600;
  }
  .back-mark .mark-row { display: flex; align-items: center; gap: 18px; }
  .back-mark .mark-square { width: 34px; height: 34px; background: var(--white); }
  .back-mark .mark-name { font-size: 72px; letter-spacing: 18px; line-height: 1; }
  .back-mark .mark-full { font-size: 17px; letter-spacing: 3px; }
</style>
</head>
<body>

<section class="card card-front" aria-label="Business card front">
  <div class="front-mark">
    <span class="mark-square"></span>
    <span class="mark-name">HSG</span>
  </div>
  <div class="front-rule"></div>

  <div class="contact">
    <h1 class="contact-name">Martin Hale</h1>
    <p class="contact-role">Manager</p>
    <ul class="contact-list">
      <li>
        <svg viewBox="0 0 16 16" aria-hidden="true"><path d="M8 1 1 7.5h2V15h4v-4h2v4h4V7.5h2z"/></svg>
        Larkspur Lane, Vermont
      </li>
      <li>
        <svg viewBox="0 0 16 16" aria-hidden="true"><path d="M4.5 0h7a1 1 0 0 1 1 1v14a1 1 0 0 1-1 1h-7a1 1 0 0 1-1-1V1a1 1 0 0 1 1-1zm.5 2v10h6V2zm3 11a1 1 0 1 0 0 2 1 1 0 0 0 0-2z"/></svg>
        0145 777 210
      </li>
      <li>
        <svg viewBox="0 0 16 16" aria-hidden="true"><path d="M3.6 1 6 3.4 4.6 5.6a10 10 0 0 0 5.8 5.8L12.6 10 15 12.4 13.4 15C6.5 15 1 9.5 1 2.6z"/></svg>
        0145 777 565
      </li>
    </ul>
  </div>
</section>

<section class="card card-back" aria-label="Business card back">
  <div class="back-mark">
    <div class="mark-row">
      <span class="mark-square"></span>
      <span class="mark-name">HSG</span>
    </div>
    <span class="mark-full">Harrowgate Structures Group</span>
  </div>
</section>

</body>
</html>
```